Buch-/E-Book-Cover Autobiographische Kurzgeschichten
Zielgruppe
Ich vermarkte mein Buch selbst. Zielgruppe sind Frauen und Männer, die leichte Lektüre mit Humor und Lebenserfahrung lesen wollen.
Aufgabenstellung
Das Buch hat den Titel 'Sturmflut ohne Ende'.
Der Inhalt sind autobiographische Kurzgeschichten.
Erst verwitwet wagte ich einen Blick über den Zaun. Und tatsächlich war dort das Gras grüner, die Wiese enthielt lebenswichtige Kräuter und bunte Blumen. Da wollte ich hier, nur wie? Ich hatte „Zäune überwinden“ nicht gelernt. Versuch und Irrtum, Feldforschung, Kampf mit mir selbst, ein nie Aufgeben führten mich zum Erfolg, auf die andere Seite. Und die Wiese hält, was sie versprach. Da hatten sich doch der Witwentröster, das Datingportal, der Escort, den ich nicht mit aufs Zimmer nahm, die Aktfotos und und und gelohnt.
Meine autobiographischen Geschichten sind wie ein gutes Parfum mit Kopf-, Herz- und Basisnote. Riech doch einfach mal rein!
Mein Logo ist zu verwenden.
Einige Kurzgeschichten aus dem Buch stehen auf meiner Website, zum Reinlesen bei Bedarf.
Die Katastrophe, der Wendepunkt in meinem Leben, war der Tod meines Mannes.
Meine Website lautet : www.tann-wiese.de

```html
<!DOCTYPE html>
<html lang="de">
<head>
<meta charset="utf-8">
<title>Sturmflut ohne Ende – Buchcover</title>
<link href="https://fonts.googleapis.com/css2?family=League+Gothic&family=Great+Vibes&family=Montserrat:wght@400;500&display=swap" rel="stylesheet">
<style>
  :root {
    --page-bg: #e9e6e1;
    --ink: #141a26;
    --outline: #ffffff;
    --storm-dark: #1d2a3c;
    --storm-mid: #4b6380;
    --storm-light: #c9d6e4;
    --fire-red: #d8342a;
    --fire-orange: #f28a1e;
    --sun-yellow: #ffd64a;
    --sun-core: #fffbe6;
    --earth: #8a5a2b;
    --hoodie: #c8102e;
    --trousers: #e4e1d8;
    --skin-tone: #e4c8aa;
  }
  * { margin: 0; padding: 0; box-sizing: border-box; }
  html, body {
    width: 1200px; height: 1068px; overflow: hidden;
    background: var(--page-bg);
  }
  .cover {
    position: absolute; left: 288px; top: 80px;
    width: 624px; height: 908px; overflow: hidden;
    box-shadow: 0 10px 30px rgba(0,0,0,.25);
  }
  .cover-scene {
    position: absolute; inset: 0;
    background:
      radial-gradient(circle at 80% 53%, var(--sun-core) 0, var(--sun-yellow) 7%, rgba(255,180,40,.85) 20%, rgba(242,138,30,0) 45%),
      radial-gradient(ellipse at 95% 28%, rgba(216,52,42,.9) 0, rgba(216,52,42,0) 40%),
      linear-gradient(180deg, rgba(0,0,0,0) 70%, rgba(138,90,43,.75) 100%),
      linear-gradient(100deg, var(--storm-dark) 0%, var(--storm-mid) 22%, var(--storm-light) 38%, #9a8c86 52%, var(--fire-orange) 72%, #6b2f3a 100%);
  }
  .cover-scene::after {
    content: ""; position: absolute; inset: 0;
    background: linear-gradient(180deg, rgba(20,26,38,.75) 0%, rgba(20,26,38,0) 35%);
  }
  .portrait {
    position: absolute; left: 502px; top: 490px; width: 122px; height: 418px;
    background: linear-gradient(180deg, var(--skin-tone) 0 12%, var(--hoodie) 12% 60%, var(--trousers) 60% 100%);
    border-radius: 40px 20px 0 0;
  }
  .publisher-mark {
    position: absolute; left: 0; right: 0; top: 66px;
    display: flex; align-items: center; justify-content: center; gap: 8px;
    font-family: "Montserrat", sans-serif; font-weight: 400;
    font-size: 15px; letter-spacing: 1px; color: var(--outline);
  }
  .publisher-mark .dot {
    width: 10px; height: 10px; border: 1.5px solid var(--outline); border-radius: 50%;
  }
  .title { position: absolute; inset: 0; width: 624px; height: 908px; }
  .title-line {
    font-family: "League Gothic", sans-serif; fill: var(--ink);
    stroke: var(--outline); stroke-width: 4px; paint-order: stroke fill;
    text-transform: uppercase;
  }
  .title-joiner {
    font-family: "Great Vibes", cursive; fill: var(--ink);
    stroke: var(--outline); stroke-width: 3px; paint-order: stroke fill;
  }
  .author {
    position: absolute; left: 0; width: 624px; top: 858px;
    text-align: center;
    font-family: "Montserrat", sans-serif; font-weight: 500;
    font-size: 18px; letter-spacing: 3px; color: var(--outline);
  }
</style>
</head>
<body>
  <main class="cover">
    <div class="cover-scene" role="img" aria-label="Unwetter mit Blitzen und Sturm links, glühende Sonne über trockener, rissiger Straße rechts"></div>
    <div class="portrait" role="img" aria-label="Porträt der Autorin in rotem Kapuzenpulli und heller Hose, an den Rand gelehnt"></div>

    <div class="publisher-mark"><span class="dot"></span>elotannwiese</div>

    <h1 class="title">
      <svg width="624" height="908" viewBox="0 0 624 908" aria-label="Sturmflut ohne Ende">
        <text class="title-line" x="84" y="298" font-size="172" textLength="456" lengthAdjust="spacingAndGlyphs">Sturmflut</text>
        <text class="title-line" x="168" y="466" font-size="200" textLength="290" lengthAdjust="spacingAndGlyphs">Ende</text>
        <text class="title-joiner" x="190" y="352" font-size="88" transform="rotate(-14 250 330)">ohne</text>
      </svg>
    </h1>

    <p class="author">AUTOR NAME</p>
  </main>
</body>
</html>
```